Willowmere Stud website

We would like to create a horse stud/agistment farm website similar to this websites we have attached below:
www.thornbrae.com.au
www.kestlewood.com.au
www.brindlecote.com
www.fenwaite.com.au
The main colour scheme are purple and white to align with the stable's racing colours.
We have also attach the company logo and also images of the farm and create some ideas for the website.
Many thanks for looking into this project!

```html
<!DOCTYPE html>
<html lang="en">
<head>
<meta charset="utf-8">
<title>Willowmere Stud</title>
<link rel="stylesheet" href="https://fonts.googleapis.com/css2?family=Crimson+Text:wght@400;600;700&family=Open+Sans:wght@400;600;700&display=swap">
<style>
:root{
  --purple:#3b1747;
  --purple-deep:#2c0f36;
  --ink:#222;
  --muted:#777;
  --paper:#fff;
  --mist:#efeff0;
  --serif:"Crimson Text", Georgia, serif;
  --sans:"Open Sans", Arial, sans-serif;
}
*{box-sizing:border-box;margin:0;padding:0}
html,body{width:1200px;height:4520px;overflow:hidden}
body{font-family:var(--sans);color:var(--ink);background:var(--paper);position:relative}
section,header,footer{position:absolute;left:0;width:1200px}
.abs{position:absolute}
.photo{position:absolute;display:block}

/* hero */
.hero{top:0;height:680px}
.hero-photo{inset:0;background:linear-gradient(180deg,#2a2a28 0%,#5d5a48 35%,#6d8b3f 70%,#4f7a2c 100%)}
.hero-horse{left:600px;top:0;width:600px;height:580px;background:radial-gradient(ellipse at 60% 45%,#5b3522 0%,#3a2216 55%,rgba(40,30,20,0) 80%)}
.topbar{top:0;left:0;width:1200px;height:120px;background:linear-gradient(180deg,rgba(44,15,54,.9),rgba(44,15,54,.55))}
.brand{left:48px;top:36px;display:flex;align-items:center;gap:12px;color:#fff;font-family:var(--sans);font-weight:600;font-size:22px}
.brand-dot{width:40px;height:40px;border-radius:50%;border:2px solid #fff}
.nav{right:36px;top:46px;display:flex;gap:30px;list-style:none}
.nav li{color:#fff;font-size:15px;font-weight:600;padding-bottom:6px}
.nav li.active{border-bottom:2px solid #fff}
.hero-title{left:84px;top:280px;color:#fff;font-weight:600;font-size:56px;line-height:64px}
.hero-tag{left:84px;top:428px;background:rgba(30,30,30,.75);color:#fff;font-size:18px;font-weight:600;padding:10px 18px}

/* section headings */
.heading{font-family:var(--serif);font-weight:700;color:var(--purple);font-size:46px;letter-spacing:1px;text-transform:uppercase;text-align:center;width:1200px;left:0}
.heading::after{content:"";display:block;width:60px;height:3px;background:var(--purple);margin:8px auto 0}

/* stallions */
.stallions{top:680px;height:920px;background:var(--paper)}
.feature{left:104px;top:140px;width:988px;height:460px;background:linear-gradient(180deg,#c9cdc8 0%,#aeb3ae 30%,#365a22 45%,#5b8a34 70%,#4a7a2a 100%)}
.feature-horse{left:480px;top:180px;width:260px;height:140px;border-radius:50%;background:radial-gradient(ellipse,#e8e0d2 0%,#d8ccb9 55%,rgba(216,204,185,0) 75%)}
.feature-name{left:40px;top:332px;color:#fff;font-family:var(--serif);font-weight:700;font-size:48px}
.feature-sub{left:40px;top:392px;color:#f2f2f2;font-size:13px}
.slide-arrows{right:0;bottom:0;display:flex;gap:4px;padding:10px}
.slide-arrows span{width:28px;height:28px;background:var(--purple);display:flex;align-items:center;justify-content:center}
.thumbs{left:104px;top:632px;display:flex;gap:26px}
.thumb{position:relative;width:312px;height:228px}
.thumb .photo{inset:0}
.thumb-name{position:absolute;left:18px;bottom:18px;color:#fff;font-family:var(--serif);font-weight:700;font-size:32px}
.side-chev{top:700px}

/* racing slider */
.racer{top:1600px;height:472px;background:var(--mist)}
.racer-panel{left:148px;top:0;width:904px;height:472px;background:var(--paper)}
.racer-photo{left:40px;top:60px;width:380px;height:360px;border-radius:40%;background:radial-gradient(ellipse,#b89a78 0%,#cdb89e 45%,rgba(255,255,255,0) 72%)}
.racer-num{left:420px;top:60px;font-family:var(--serif);font-size:280px;font-weight:700;color:#e6e6e6;line-height:1}
.racer-text{left:540px;top:150px;width:250px;font-family:var(--serif);font-size:18px;line-height:24px;color:#333}
.circle-btn{width:52px;height:52px;border-radius:50%;border:2px solid #aaa;background:#fff;display:flex;align-items:center;justify-content:center}

/* news */
.news{top:2072px;height:688px;background:var(--paper)}
.news-title{left:80px;top:70px;font-family:var(--serif);font-weight:700;font-size:46px;color:var(--purple-deep)}
.view-all{right:112px;top:92px;font-family:var(--serif);font-weight:700;font-size:17px;color:var(--purple-deep)}
.cards{left:80px;top:148px;display:flex;gap:72px}
.card{width:288px}
.card-img{position:relative;height:212px}
.card h3{font-family:var(--serif);font-weight:700;font-size:18px;line-height:24px;margin-top:14px}
.card-date{display:flex;align-items:center;gap:8px;font-size:13px;margin-top:10px;color:#333}
.card p{font-size:13px;line-height:20px;color:var(--muted);margin-top:12px}
.btn{display:inline-block;background:var(--purple);color:#fff;font-family:var(--serif);font-weight:700;font-size:15px;padding:10px 18px;margin-top:22px;letter-spacing:.5px}

/* gallery */
.gallery{top:2760px;height:420px;background:linear-gradient(180deg,#f3f3f3,#e9e9ea)}
.gallery .heading{top:40px}
.gal-row{left:32px;top:140px;display:flex;gap:32px}
.gal-row .photo{position:relative;width:260px;height:212px}
.dots{left:0;width:1200px;top:384px;display:flex;justify-content:center;gap:8px}
.dots span{width:10px;height:10px;border-radius:50%;border:1px solid #888;background:#fff}
.dots span.on{background:var(--purple);border-color:var(--purple)}

/* newsletter */
.newsletter{top:3180px;height:400px;background:var(--paper)}
.mail-icon{left:570px;top:90px}
.newsletter .heading{top:156px}
.newsletter .heading::after{display:none}
.news-sub{left:0;width:1200px;top:228px;text-align:center;font-size:15px;color:var(--muted)}
.signup{left:240px;top:284px;display:flex;gap:20px}
.signup-input{width:520px;height:56px;border:1px solid #ccc;font-size:14px;color:#999;padding:18px 14px}
.signup-btn{width:190px;height:56px;background:var(--purple);color:#fff;font-family:var(--serif);font-weight:700;font-size:22px;display:flex;align-items:center;justify-content:center;letter-spacing:1px}

/* banner */
.banner{top:3580px;height:420px}
.banner .photo{inset:0;background:linear-gradient(90deg,#3a2416 0%,#6b4327 30%,#8a5a33 55%,#5f3c22 80%,#2f1d12 100%)}
.banner-text{left:0;width:1200px;top:186px;text-align:center;color:#fff;font-family:var(--serif);font-weight:700;font-size:40px}

/* footer */
.site-footer{top:4000px;height:520px;background:var(--purple)}
.foot-brand{left:0;width:1200px;top:44px;display:flex;flex-direction:column;align-items:center;gap:10px;color:#fff;font-weight:600;font-size:22px}
.foot-brand .brand-dot{width:44px;height:44px}
.foot-cols{left:80px;top:170px;display:flex}
.foot-col{width:265px;color:#fff}
.foot-col h4{font-weight:700;font-size:17px;letter-spacing:1px;text-transform:uppercase;margin-bottom:18px}
.foot-col ul{list-style:none}
.foot-col li{font-size:13px;line-height:22px;color:#ddd}
.contact-row{display:flex;gap:12px;align-items:flex-start;font-size:13px;color:#ddd;margin-bottom:14px;line-height:19px}
.social{display:flex;align-items:center;gap:14px;margin-bottom:16px;font-size:13px;color:#ddd}
.social span{width:38px;height:38px;border-radius:50%;background:#6a4a7a}
.copyright{left:0;width:1200px;top:440px;border-top:1px solid rgba(255,255,255,.15);padding-top:24px;text-align:center;font-size:13px;color:#ccc}
</style>
</head>
<body>

<header class="hero">
  <div class="photo hero-photo" role="img" aria-label="Rider on a bay horse in a green arena under an overcast sky"></div>
  <div class="photo hero-horse" role="img" aria-label="Dressage horse with braided mane and rider in black boots"></div>
  <div class="abs topbar"></div>
  <div class="abs brand"><span class="brand-dot"></span>Willowmere Stud</div>
  <ul class="abs nav">
    <li class="active">Home</li><li>Stallions</li><li>News</li><li>Sales</li><li>Gallery</li><li>About</li><li>Contact</li>
  </ul>
  <h1 class="abs hero-title">Our kingdom For<br>A Horse</h1>
  <p class="abs hero-tag">Inter relation Between Horse &amp; Rider</p>
</header>

<section class="stallions">
  <h2 class="abs heading" style="top:56px">Stallions</h2>
  <div class="photo feature" role="img" aria-label="Grey stallion standing in a green paddock lined with trees">
    <div class="photo feature-horse"></div>
    <div class="abs feature-name">Velvet Regent</div>
    <div class="abs feature-sub">Lorem Ipsum is simply dummy text of the printing and typesetting.</div>
    <div class="abs slide-arrows">
      <span><svg width="10" height="12" viewBox="0 0 10 12"><path d="M7 1 2 6l5 5" fill="none" stroke="#fff" stroke-width="2"/></svg></span>
      <span><svg width="10" height="12" viewBox="0 0 10 12"><path d="M3 1l5 5-5 5" fill="none" stroke="#fff" stroke-width="2"/></svg></span>
    </div>
  </div>
  <svg class="abs side-chev" style="left:50px" width="20" height="40" viewBox="0 0 20 40"><path d="M16 4 4 20l12 16" fill="none" stroke="#ccc" stroke-width="3"/></svg>
  <svg class="abs side-chev" style="left:1130px" width="20" height="40" viewBox="0 0 20 40"><path d="M4 4l12 16L4 36" fill="none" stroke="#ccc" stroke-width="3"/></svg>
  <div class="abs thumbs">
    <div class="thumb"><div class="photo" role="img" aria-label="Mare and foal grazing by a white fence" style="background:linear-gradient(180deg,#9fb6a0 0%,#6f8f52 45%,#4d7a2e 100%)"></div><span class="thumb-name">Riverlark</span></div>
    <div class="thumb"><div class="photo" role="img" aria-label="Chestnut horse trotting in a field" style="background:linear-gradient(180deg,#c9d3d8 0%,#a89a7a 50%,#6f8a3c 100%)"></div><span class="thumb-name">Brave Thistle</span></div>
    <div class="thumb"><div class="photo" role="img" aria-label="Group of horses galloping across a meadow" style="background:linear-gradient(180deg,#8a7a5a 0%,#6b3d24 50%,#5a6a2c 100%)"></div><span class="thumb-name">Ever So Willing</span></div>
  </div>
</section>

<section class="racer">
  <div class="abs racer-panel">
    <div class="photo racer-photo" role="img" aria-label="Jockey in bright silks riding a galloping racehorse"></div>
    <div class="abs racer-num">01</div>
    <p class="abs racer-text">Lorem Ipsum is simply dummy text of the printing and typesetting industry. Lorem Ipsum has been the industry.</p>
  </div>
  <div class="abs circle-btn" style="left:40px;top:210px"><svg width="12" height="16" viewBox="0 0 12 16"><path d="M9 2 3 8l6 6" fill="none" stroke="#888" stroke-width="2"/></svg></div>
  <div class="abs circle-btn" style="left:1108px;top:210px"><svg width="12" height="16" viewBox="0 0 12 16"><path d="M3 2l6 6-6 6" fill="none" stroke="#888" stroke-width="2"/></svg></div>
</section>

<section class="news">
  <h2 class="abs news-title">LATEST NEWS</h2>
  <span class="abs view-all">VIEW ALL...&gt;&gt;</span>
  <div class="abs cards">
    <article class="card">
      <div class="photo card-img" role="img" aria-label="Rider on a chestnut horse in autumn woodland" style="background:linear-gradient(180deg,#b08a5a 0%,#8a5a2c 55%,#4a3a22 100%)"></div>
      <h3>Lorem Ipsum is simply dummy text of the printing and typesetting.</h3>
      <div class="card-date"><svg width="14" height="14" viewBox="0 0 14 14"><rect x="1" y="2" width="12" height="11" fill="none" stroke="#333"/><path d="M1 5h12M4 0v3M10 0v3" stroke="#333"/></svg>07 March 2016</div>
      <p>Lorem Ipsum is simply dummy text of the printing and typesetting industry. Lorem Ipsum has been the industry is simply dummy text.</p>
      <span class="btn">READ MORE</span>
    </article>
    <article class="card">
      <div class="photo card-img" role="img" aria-label="Dark horse galloping through mist" style="background:linear-gradient(180deg,#8fa6b4 0%,#6b6055 55%,#3a2e26 100%)"></div>
      <h3>Lorem Ipsum is simply dummy text of the printing and typesetting.</h3>
      <div class="card-date"><svg width="14" height="14" viewBox="0 0 14 14"><rect x="1" y="2" width="12" height="11" fill="none" stroke="#333"/><path d="M1 5h12M4 0v3M10 0v3" stroke="#333"/></svg>07 March 2016</div>
      <p>Lorem Ipsum is simply dummy text of the printing and typesetting industry. Lorem Ipsum.</p>
      <span class="btn">READ MORE</span>
    </article>
    <article class="card">
      <div class="photo card-img" role="img" aria-label="Horses running through a dusty paddock" style="background:linear-gradient(180deg,#d8d2c6 0%,#b8a88e 55%,#8a7a5e 100%)"></div>
      <h3>Lorem Ipsum is simply dummy text of the printing and typesetting.</h3>
      <div class="card-date"><svg width="14" height="14" viewBox="0 0 14 14"><rect x="1" y="2" width="12" height="11" fill="none" stroke="#333"/><path d="M1 5h12M4 0v3M10 0v3" stroke="#333"/></svg>07 March 2016</div>
      <p>Lorem Ipsum is simply dummy text of the printing and typesetting industry. Lorem Ipsum.</p>
      <span class="btn">READ MORE</span>
    </article>
  </div>
</section>

<section class="gallery">
  <h2 class="abs heading">Our Gallery</h2>
  <div class="abs gal-row">
    <div class="photo" role="img" aria-label="Two horses grazing in a lush field" style="background:linear-gradient(180deg,#5a6e44 0%,#4f6a2e 100%)"></div>
    <div class="photo" role="img" aria-label="Paddock with wooden fence under a blue sky" style="background:linear-gradient(180deg,#6f8fb8 0%,#c0b08a 50%,#5a7a2e 100%)"></div>
    <div class="photo" role="img" aria-label="Row of horses standing together on grass" style="background:linear-gradient(180deg,#b8c8d8 0%,#6a5040 55%,#5a7a34 100%)"></div>
    <div class="photo" role="img" aria-label="Tree-lined driveway leading to the farm" style="background:linear-gradient(180deg,#3e5a2a 0%,#6a7e3a 60%,#b89a70 100%)"></div>
  </div>
  <div class="abs dots"><span></span><span class="on"></span><span></span><span></span><span></span></div>
</section>

<section class="newsletter">
  <svg class="abs mail-icon" width="60" height="46" viewBox="0 0 60 46"><rect x="2" y="2" width="56" height="42" fill="none" stroke="#ccc" stroke-width="3"/><path d="M2 2l28 24L58 2" fill="none" stroke="#ccc" stroke-width="3"/></svg>
  <h2 class="abs heading">Sign Up For Newsletter</h2>
  <p class="abs news-sub">Would you like to receive our exclusive news and update for sign up our newsletter?</p>
  <div class="abs signup">
    <div class="signup-input">Enter Email *</div>
    <div class="signup-btn">SUBSCRIBE</div>
  </div>
</section>

<section class="banner">
  <div class="photo" role="img" aria-label="Close group of brown horses in warm light"></div>
  <p class="abs banner-text">We've Made A life That Will Change You</p>
</section>

<footer class="site-footer">
  <div class="abs foot-brand"><span class="brand-dot"></span>Willowmere Stud</div>
  <div class="abs foot-cols">
    <div class="foot-col">
      <h4>Sitemap</h4>
      <ul><li>Home</li><li>Stallions</li><li>News</li><li>Sales</li><li>Gallery</li><li>About</li><li>Contact</li></ul>
    </div>
    <div class="foot-col">
      <h4>Satallions</h4>
      <ul><li>At Stud Now</li><li>Velvet Regent</li><li>Riverlark</li><li>Ever So Willing</li><li>Brave Thistle</li><li>Silver Halberd</li><li>North Lantern</li></ul>
    </div>
    <div class="foot-col">
      <h4>Contact Us</h4>
      <div class="contact-row"><svg width="14" height="18" viewBox="0 0 14 18"><path d="M7 17S1 10 1 6.5a6 6 0 0 1 12 0C13 10 7 17 7 17z" fill="#fff"/><circle cx="7" cy="6.5" r="2" fill="#3b1747"/></svg><div><strong style="color:#fff">Willowmere Stud</strong><br>121 - Lorem ipsum simple text<br>of print and type industry</div></div>
      <div class="contact-row"><svg width="14" height="14" viewBox="0 0 14 14"><path d="M3 1l3 3-2 2a8 8 0 0 0 4 4l2-2 3 3-2 2C5 13 1 9 1 3z" fill="#fff"/></svg>000 555 0199</div>
      <div class="contact-row"><svg width="14" height="12" viewBox="0 0 14 12"><rect x="1" y="1" width="12" height="10" fill="none" stroke="#fff"/><path d="M1 1l6 5 6-5" fill="none" stroke="#fff"/></svg>info@willowmerestud.example</div>
    </div>
    <div class="foot-col">
      <h4>Follow Us</h4>
      <div class="social"><span></span>Paddockbook</div>
      <div class="social"><span></span>Whinnyline</div>
      <div class="social"><span></span>Stallgram</div>
    </div>
  </div>
  <p class="abs copyright">Willowmere Stud, 2016 All Rights Reserved.</p>
</footer>

</body>
</html>
```